UK garage/funky house night flier

I need a flier design to upload to my socialpagehub event page and also some printed fliers to promote the event.

Event is in an urban area underneath railway arches so would like a flier to reflect this with an urban background.
Updates

new photos uploaded to be used as possible backgrounds

Target Market(s)

aged 18-30

Industry/Entity Type

House

Requirements
Must have
• The following text on front of flier:

MIDNIGHT KREST PROMOTIONS PRESENTS A NIGHT CALLED…

‘COPPER TUNNEL RHYTHMZ’

Saturday 7th September 2013

@ Dock27, Marlow Lane, Digbeth, Birmingham B7 3QX

9pm till late

DJ’s playing a selection of Funky house/deep house/future garage and old school 2-step garage

(On back of flier......)

Come and enjoy yourself in a friendly, safe environment with like-minded people who are out to have a good time and rave till the early hours. This venue is part outdoor terrace and part indoor with music being played on the Sonorix-Max Soundsystem – so you know it is a night not to be missed!!

This event is guestlist only. Those not on the guest list will not be allowed entry. To get yourself on the guest list go to the socialpagehub page www.socialpagehub.example/midnightkrestpromotions and join the event ‘Copper Tunnel Rhythmz’

Dresscode: smart. No trainers/tracksuits
Admission fee on the door is £5
Last entry: midnight
Nice to have
• must be portrait, A5 or A6 size

Urban background, maybe at night, a street with old brickwork, maybe some speakers in the foreground.

Dock27 plain text mark bottom right

Back of flier to have the map of Dock27

```html
<!DOCTYPE html>
<html lang="en">
<head>
<meta charset="utf-8">
<title>Copper Tunnel Rhythmz – Flier Front and Back</title>
<link rel="stylesheet" href="https://fonts.googleapis.com/css2?family=Open+Sans:wght@400;600&family=Audiowide&family=Kurale&display=swap">
<style>
  :root {
    --stage: #1f2326;
    --navy-top: #0c1a4a;
    --navy-deep: #050a26;
    --band-blue: #1b2f9c;
    --white: #ffffff;
    --neon: #bff6ff;
    --neon-glow: #38c8ff;
    --lime: #d9f23a;
    --yellow: #e8f24a;
    --green-text: #c6ff4a;
    --pink: #ff4fcf;
    --frame-black: #000000;
    --map-grey: #e9e9e9;
  }
  * { margin: 0; padding: 0; box-sizing: border-box; }
  html, body { width: 1200px; height: 1000px; overflow: hidden; background: var(--stage); }
  .canvas { position: relative; width: 1200px; height: 1000px; background: var(--stage); }

  /* ---------- Front ---------- */
  .flier-front {
    position: absolute; left: 66px; top: 108px; width: 518px; height: 735px;
    background: linear-gradient(180deg, var(--navy-deep) 0%, var(--navy-top) 30%, #101d55 32%);
    overflow: hidden;
  }
  .front-photo {
    position: absolute; left: 0; top: 235px; width: 518px; height: 479px;
    background:
      radial-gradient(ellipse 60% 45% at 62% 62%, rgba(60,110,255,0.55) 0%, rgba(60,110,255,0) 70%),
      radial-gradient(ellipse 55% 60% at 15% 55%, rgba(200,80,20,0.85) 0%, rgba(120,40,10,0) 75%),
      linear-gradient(180deg, #0b0b14 0%, #1a1220 20%, #4a2410 55%, #b5521c 85%, #d4682a 100%);
  }
  .front-band {
    position: absolute; left: 0; bottom: 0; width: 518px; height: 21px;
    background: linear-gradient(90deg, #0b1a6e, var(--band-blue), #0b1a6e);
  }
  .presents {
    position: absolute; left: 0; top: 26px; width: 518px;
    font: 400 22px/30px "Open Sans", sans-serif; color: var(--white);
    text-align: center; letter-spacing: 0.3px;
  }
  .event-title {
    position: absolute; left: 0; top: 96px; width: 518px;
    font: 400 34px/58px "Audiowide", sans-serif; color: var(--neon);
    text-align: center; letter-spacing: 2px;
    text-shadow: 0 0 4px var(--neon-glow), 0 0 10px var(--neon-glow), 0 0 18px rgba(56,200,255,0.6);
  }
  .music-line {
    position: absolute; left: 16px; top: 248px; width: 495px;
    font: 400 18px/27px "Open Sans", sans-serif; color: var(--yellow);
  }
  .event-details {
    position: absolute; left: 0; top: 592px; width: 518px; text-align: center;
    font-family: "Open Sans", sans-serif; color: var(--yellow);
  }
  .event-date { font-size: 20px; line-height: 30px; }
  .event-venue { font-size: 14.5px; line-height: 26px; margin-top: 4px; }
  .event-time { font-size: 14.5px; line-height: 26px; margin-top: 2px; }
  .venue-mark {
    position: absolute; left: 401px; top: 669px; width: 97px; height: 44px;
    background: var(--white);
    display: flex; align-items: center; justify-content: center; gap: 6px;
  }
  .venue-mark-square { width: 9px; height: 9px; background: #5a5a5a; }
  .venue-mark-name { font: 400 16px/1 "Open Sans", sans-serif; color: #5a5a5a; }

  /* ---------- Back ---------- */
  .flier-back {
    position: absolute; left: 608px; top: 108px; width: 521px; height: 735px;
    background:
      radial-gradient(ellipse 40% 30% at 90% 10%, rgba(120,150,255,0.7) 0%, rgba(0,0,0,0) 70%),
      radial-gradient(ellipse 35% 25% at 10% 90%, rgba(90,120,255,0.6) 0%, rgba(0,0,0,0) 70%),
      linear-gradient(135deg, #1d2a9a 0%, #0a0f3c 45%, #23309e 100%);
  }
  .back-frame {
    position: absolute; left: 14px; top: 14px; width: 493px; height: 708px;
    border: 6px solid var(--frame-black);
    background:
      radial-gradient(ellipse 55% 35% at 70% 35%, rgba(70,90,200,0.45) 0%, rgba(0,0,0,0) 70%),
      radial-gradient(ellipse 50% 30% at 30% 70%, rgba(60,80,190,0.35) 0%, rgba(0,0,0,0) 70%),
      linear-gradient(180deg, #05060f 0%, #0a0d25 50%, #05060f 100%);
  }
  .back-copy {
    position: absolute; left: 14px; top: 40px; width: 470px;
    font: 400 15.5px/24.5px "Kurale", serif; color: var(--green-text);
  }
  .back-copy p + p { margin-top: 0; }
  .highlight { font-size: 19px; line-height: 28px; color: var(--pink); }
  .guest-note { margin-top: 6px; }
  .guestlist-tag { color: var(--pink); font-style: italic; font-size: 18px; }
  .signup-link {
    margin: 12px 0 0 42px; color: var(--pink); font-style: italic; font-size: 16.5px; line-height: 26px;
  }
  .door-info { margin-top: 14px; text-align: center; line-height: 26px; }
  .venue-map {
    position: absolute; left: 75px; top: 453px; width: 337px; height: 217px;
    background: linear-gradient(135deg, #f4f4f4 0%, var(--map-grey) 50%, #d6d6d6 100%);
  }
</style>
</head>
<body>
<div class="canvas">

  <section class="flier-front">
    <div class="front-photo" role="img" aria-label="Night photo of brick railway arches in Digbeth with blue light-painting trails over the street"></div>
    <div class="front-band"></div>

    <p class="presents">MIDNIGHT KREST PROMOTIONS PRESENTS<br>A NIGHT CALLED...</p>
    <h1 class="event-title">COPPER TUNNEL<br>RHYTHMZ</h1>

    <p class="music-line">DJ’s playing a selection of Funky house/deep house/future garage and old school 2-step garage</p>

    <div class="event-details">
      <p class="event-date">Saturday 7th September 2013</p>
      <p class="event-venue">@ Dock27, Marlow Lane, Digbeth, Birmingham B7 3QX</p>
      <p class="event-time">9pm till late</p>
    </div>

    <div class="venue-mark">
      <span class="venue-mark-square"></span>
      <span class="venue-mark-name">Dock27</span>
    </div>
  </section>

  <section class="flier-back">
    <div class="back-frame">
      <div class="back-copy">
        <p>Come and enjoy yourself in a friendly, safe environment with like-minded people who are out to have a good time and rave till the early hours.</p>
        <p>This venue is part outdoor terrace and part indoor with music being played on the Sonorix-MaxSoundsystem</p>
        <p class="highlight">so you know it is a night not to be missed!</p>
        <p class="guest-note">This event is <span class="guestlist-tag">guestlist only</span>. Those not on the guest list will not be allowed entry. To get yourself on the guest list go to the socialpagehub page</p>
        <p class="signup-link">www.socialpagehub.example/midnightkrestpromotions<br>and join the event ‘Copper Tunnel Rhythmz’</p>
        <div class="door-info">
          <p>Dresscode: smart. No trainers/tracksuits</p>
          <p>Admission fee on the door is £5</p>
          <p>Last entry: midnight</p>
        </div>
      </div>
      <div class="venue-map" role="img" aria-label="Street map of Digbeth showing the route from the city centre to Dock27 on Marlow Lane"></div>
    </div>
  </section>

</div>
</body>
</html>
```